Business Card Design

Business sales of reconditioned / used batteries with mobile delivery and install services. Customers base majority are auto car sales lots and individuals.

Card need to convey quality product reliability and quick prompt professional service.

Card must reflect excellence in customer care and product being offered

Target Market(s)

Auto car lots new and used. Auto repair shops. Individuals.

Industry/Entity Type

Business

Contact Information for Business Card

Batteries Q-Volt
Cars, Trucks, Boats, Motorcycles, lawn mowers, power tools
Delivery & install available most vehicles
Mon-Sat 9-6pm
Dale Morrick 501-738-2056
*product warranty 6 month shelf life battery/1 year blems battery

```html
<!DOCTYPE html>
<html lang="en">
<head>
<meta charset="utf-8">
<title>Batteries Q-Volt — Business Card</title>
<link rel="stylesheet" href="https://fonts.googleapis.com/css2?family=Oswald:wght@600&family=Open+Sans:wght@600;700&display=swap">
<style>
  :root {
    --page-bg: #ffffff;
    --card-light: #f4f4f4;
    --card-mid: #d9d9d9;
    --photo-dark: #9a9a9a;
    --brand-red: #c8161d;
    --band-red: #b51218;
    --band-ink: #1a1a1a;
    --card-black: #121212;
    --card-black-2: #262626;
    --text-white: #ffffff;
    --logo-ink: #1c1c1c;
  }
  html, body {
    margin: 0;
    width: 1200px;
    height: 900px;
    overflow: hidden;
    background: var(--page-bg);
  }
  .canvas {
    position: relative;
    width: 1200px;
    height: 900px;
  }
  .business-card {
    position: absolute;
    left: 75px;
    top: 150px;
    width: 1050px;
    height: 600px;
    border-radius: 40px;
    overflow: hidden;
    box-shadow: 0 18px 40px rgba(0,0,0,0.18);
  }
  .card-header {
    position: absolute;
    inset: 0 0 auto 0;
    height: 292px;
    background: linear-gradient(180deg, var(--card-mid) 0%, var(--card-light) 55%, #ffffff 100%);
  }
  .header-photo {
    position: absolute;
    right: 0;
    top: 0;
    width: 330px;
    height: 292px;
    background: linear-gradient(200deg, #cfcfcf 0%, var(--photo-dark) 70%, #7d7d7d 100%);
    opacity: 0.85;
  }
  .brand-name {
    position: absolute;
    left: 88px;
    top: 128px;
    margin: 0;
    font-family: "Oswald", sans-serif;
    font-weight: 600;
    font-size: 84px;
    line-height: 1;
    letter-spacing: 2px;
    text-transform: uppercase;
    color: var(--logo-ink);
  }
  .service-band {
    position: absolute;
    left: 0;
    right: 0;
    top: 292px;
    height: 40px;
    background: var(--band-red);
    display: flex;
    align-items: center;
    justify-content: center;
    font-family: "Oswald", sans-serif;
    font-weight: 600;
    font-size: 25px;
    letter-spacing: 0.5px;
    text-transform: uppercase;
    color: var(--band-ink);
    white-space: nowrap;
  }
  .card-body {
    position: absolute;
    left: 0;
    right: 0;
    top: 332px;
    bottom: 0;
    background: linear-gradient(180deg, var(--card-black-2) 0%, var(--card-black) 100%);
    text-align: center;
    font-family: "Open Sans", sans-serif;
  }
  .opening-hours {
    margin: 16px 0 0;
    font-weight: 700;
    font-size: 30px;
    color: var(--text-white);
  }
  .contact-name {
    margin: 18px 0 0;
    font-weight: 600;
    font-size: 42px;
    color: var(--brand-red);
  }
  .contact-phone {
    margin: 6px 0 0;
    font-weight: 600;
    font-size: 44px;
    color: var(--text-white);
  }
  .warranty-note {
    margin: 22px 0 0;
    font-weight: 700;
    font-size: 27px;
    color: var(--brand-red);
  }
</style>
</head>
<body>
<main class="canvas">
  <section class="business-card">
    <header class="card-header">
      <div class="header-photo" role="img" aria-label="Photo of a car battery with jumper cable clamps on its terminals"></div>
      <h1 class="brand-name">Batteries Q-Volt</h1>
    </header>
    <div class="service-band">Cars, Trucks, Boats, Motorcycles, Lawn Mowers, Power Tools Delivery &amp; Install</div>
    <div class="card-body">
      <p class="opening-hours">Mon-Sat : 9.00 am to 6.00 pm</p>
      <p class="contact-name">Dale Morrick</p>
      <p class="contact-phone">501-738-2056</p>
      <p class="warranty-note">*product warranty 6 month shelf life battery/1 year blems battery</p>
    </div>
  </section>
</main>
</body>
</html>
```